Business Card Design for LeafCrest (Farming Devices)

We need Business Cards for our new Company based in Switzerland called "LeafCrest" We develop innovativ products for indoor and outdoor Farming for household and components for vertical farming. Our initial BloomNest gives people the possibility to grow their own food at home all year round. The design should communicate freshness, innovation, health.

```html
<!DOCTYPE html>
<html lang="en">
<head>
<meta charset="utf-8">
<title>LeafCrest Business Card</title>
<link rel="stylesheet" href="https://fonts.googleapis.com/css2?family=Lato:wght@700&family=Barlow:wght@600&family=Ubuntu:wght@400&display=swap">
<style>
  :root {
    --backdrop: #c5c9d2;
    --forest: #22763a;
    --leaf: #79b642;
    --ink: #1f6d36;
    --paper: #ffffff;
  }
  * { margin: 0; padding: 0; box-sizing: border-box; }
  html, body { width: 1200px; height: 1200px; overflow: hidden; background: var(--backdrop); }
  .stage { position: relative; width: 1200px; height: 1200px; }

  .card { position: absolute; width: 358px; height: 644px; overflow: hidden; }
  .card--front { left: 225px; top: 259px; background: var(--forest); }
  .card--back { left: 660px; top: 261px; background: var(--forest); }

  .brand-name {
    position: absolute; left: 0; width: 100%; text-align: center;
    font-family: "Lato", sans-serif; font-weight: 700; color: var(--paper);
    letter-spacing: 0.5px; line-height: 1;
  }
  .card--front .brand-name { top: 298px; font-size: 46px; }
  .card--back .brand-name { top: 80px; font-size: 38px; }

  .plant-art--front {
    position: absolute; left: 130px; top: 356px; width: 98px; height: 268px;
    border-radius: 6px;
    background: linear-gradient(180deg, rgba(121,182,66,0.10) 0%, rgba(121,182,66,0.30) 100%);
  }

  .arc-band { position: absolute; left: 0; top: 0; width: 358px; height: 644px; }

  .person-name {
    position: absolute; left: 51px; top: 283px;
    font-family: "Barlow", sans-serif; font-weight: 600; font-size: 28px;
    color: var(--ink); letter-spacing: 0.8px; line-height: 1;
  }
  .person-title {
    position: absolute; left: 51px; top: 322px;
    font-family: "Barlow", sans-serif; font-weight: 600; font-size: 22px;
    color: var(--ink); letter-spacing: 0.6px; line-height: 1;
  }

  .plant-art--back {
    position: absolute; left: 14px; top: 406px; width: 60px; height: 228px;
    border-radius: 6px;
    background: linear-gradient(180deg, rgba(121,182,66,0.14) 0%, rgba(121,182,66,0.32) 100%);
  }

  .contact-icons { position: absolute; left: 48px; top: 476px; width: 24px; height: 108px; }
  .contact-list {
    position: absolute; left: 81px; top: 479px; list-style: none;
    font-family: "Ubuntu", sans-serif; font-size: 19.5px; color: var(--ink);
    letter-spacing: 0.4px;
  }
  .contact-list li { height: 28px; line-height: 20px; }
</style>
</head>
<body>
<main class="stage">

  <section class="card card--front" aria-label="Card front">
    <div class="brand-name">LeafCrest</div>
    <div class="plant-art--front" role="img" aria-label="Illustration of a young plant with long stem and roots"></div>
  </section>

  <section class="card card--back" aria-label="Card back">
    <svg class="arc-band" viewBox="0 0 358 644" aria-hidden="true">
      <path fill="var(--leaf)" d="M0,251 C50,175 110,146 173,146 C260,146 330,200 358,273 L358,644 L0,644 Z"/>
      <path fill="var(--paper)" d="M0,251 C40,195 100,165 154,165 C230,165 285,215 315,258 Q322,268 335,267 L358,267 L358,644 L0,644 Z"/>
    </svg>
    <div class="brand-name">LeafCrest</div>

    <div class="person-name">NAME SURNAME</div>
    <div class="person-title">your title</div>

    <div class="plant-art--back" role="img" aria-label="Illustration of a sprout with leaves and roots"></div>

    <svg class="contact-icons" viewBox="0 0 24 108" aria-hidden="true" fill="none" stroke="var(--leaf)" stroke-width="1.6">
      <circle cx="12" cy="12" r="10" fill="var(--paper)"/>
      <path d="M12,18 C8,13 8,11 8,10 A4,4 0 0 1 16,10 C16,11 16,13 12,18 Z"/>
      <circle cx="12" cy="10" r="1.5"/>
      <circle cx="12" cy="40" r="10" fill="var(--paper)"/>
      <path d="M8,36 Q9,34 10,35 L11,37 Q10,38 11,40 Q13,43 14,42 L16,43 Q17,45 15,45 Q11,45 8,40 Q7,38 8,36 Z" fill="var(--leaf)" stroke="none"/>
      <circle cx="12" cy="68" r="10" fill="var(--paper)"/>
      <text x="12" y="73" text-anchor="middle" font-family="Ubuntu, sans-serif" font-size="14" font-weight="700" fill="var(--leaf)" stroke="none">@</text>
      <circle cx="12" cy="96" r="10" fill="var(--paper)"/>
      <circle cx="12" cy="96" r="6.5"/>
      <ellipse cx="12" cy="96" rx="3" ry="6.5"/>
      <line x1="5.5" y1="96" x2="18.5" y2="96"/>
    </svg>

    <ul class="contact-list">
      <li>your company address</li>
      <li>00 1234 1234</li>
      <li>email@yourcompany.com</li>
      <li>www.yourcompany.com</li>
    </ul>
  </section>

</main>
</body>
</html>
```